Zielgruppe
HANDARBEIT
HAT SEELE.
»80 % gibt uns die Natur vor,
für die restlichen 20 % geben wir alles!«
Lorenz Habichtsberg
Seit über 125 Jahren ist die Rotweinstadt Ingelheim Sitz unseres Familienbetriebes. Im alten Ober-Ingelheimer Schulhaus gelegen, betreiben wir das Weingut in der nunmehr 5. Generation. Unser hoher Qualitätsanspruch und Traditionsbewusstsein wird von Kennern eines guten Weines geschätzt. Zusammen mit der Natur und so schonend wie möglich bewirtschaften wir die rund 15 ha Weinberge in den besten Lagen Ingelheims.
Ganz in der Tradition Karls des Großen, der die Rotweinreben um 800 n. Chr. nach Ingelheim brachte, sind die Spät- und Frühburgunder die Spezialitäten unseres Hauses. Seit 2015 sind wir Träger des „Goldenen Rebenpokals' des Weinkulturmagazins Traubia. Das macht uns stolz und gibt uns Energie. Auch die Rieslinge und die weißen Burgundersorten stehen im Fokus und werden mit viel Gefühl zum Detail gekeltert. Den geselligen Mittelpunkt des Weinguts bildet unser über hundert Jahre alter Pavillon. Er steht symbolisch für uns als gastliche Weinfamilie und vertritt unser Weingut auch nach außen auf unseren Etiketten.
Aufgabenstellung
Ein Wein für FRANKFURTER
Wir möchten für einen führende Marktal-Gruppe in Frankfurt eine Weißwein-Sonderedition entwickeln.
Es soll ein Label sein, womit sich jeder Frankfurter identifizieren kann (Skyline gab es schon mal ist aber nicht ausgeschlossen) und dazu animiert wird die Weinflasche blind zu kaufen.
Die Rebsorte soll auf dem Vorderetikett genannt werden. Es ist ein Grauburgunder oder Grauer Burgunder. Der Wein soll ein schönes Mitbringsel oder auch für den eigenen Genuss sein. Die Flasche wird sich im mittleren Preissegment bewegen +/- 10€ im Verkauf. Zielgruppe 40-65 Jahre alt.
Es gibt drei mögliche Etikettengrößen.
Variante 1: Bestehendes Habichtsberg-Etikett mit Streifen (wie in der Anlage)
Variante 2: Vorder- und Rückenetikett mit je 7cm x 7cm oder
Variante 3: Vorderetikett (9cm Breit x 6cm hoch) und Rückenetikett (7cm Breit x 6cm hoch)
Die Rückseite kann ein : gestalterisches Element vom Vorderetikett beinhalten, ist aber durch die gesetzlichen Angaben und den EAN-Code schon ziemlich ausgelastet. Es zum größten Teil um das Vorderetikett.
Die Kapsel am Flaschenhals ist weiß mit gelber Markierung und es gibt eine gelbe Kapsel mit weißer Markierung. Diese ist beiden sind fix, da der Wein schon abgefüllt ist. Es ist eine Burgunderflasche.
Ein Flaschenbild stelle ich zur Verfügung.

```html
<!DOCTYPE html>
<html lang="de">
<head>
<meta charset="utf-8">
<title>Grauburgunder Etiketten – Weingut Habichtsberg</title>
<link rel="stylesheet" href="https://fonts.googleapis.com/css2?family=Montserrat:wght@300;400;800&display=swap">
<style>
  :root {
    --canvas: #ededee;
    --paper: #ffffff;
    --ink: #1a1a1a;
    --amber-dark: #d18e2f;
    --amber-light: #f8ad2a;
    --amber: #f2a62d;
    --illus-a: #f4f4f4;
    --illus-b: #d9d9d9;
  }
  * { margin: 0; padding: 0; box-sizing: border-box; }
  html, body { width: 1200px; height: 900px; overflow: hidden; }
  body {
    position: relative;
    background: var(--canvas);
    font-family: "Montserrat", sans-serif;
    color: var(--ink);
  }
  .label {
    position: absolute;
    background: var(--paper);
    box-shadow: 0 1px 4px rgba(0,0,0,.18);
    overflow: hidden;
  }
  .label--amber { background: linear-gradient(90deg, var(--amber-dark), var(--amber-light)); }
  .label__stripes { position: absolute; inset: 0; width: 100%; height: 100%; }
  .label__art {
    position: absolute;
    border-radius: 50%;
    background: radial-gradient(circle at 50% 40%, var(--illus-a), var(--illus-b));
    border: 1px solid var(--ink);
  }
  .label--amber .label__art { background: radial-gradient(circle at 50% 40%, #f7b541, #e0962a); }
  .label__text { position: absolute; line-height: 1; }
  .label__kicker { font-weight: 400; letter-spacing: .16em; font-size: 16px; }
  .label__variety { font-weight: 800; }
  .label__vintage { font-weight: 300; }
  .label__winery {
    position: absolute;
    font-weight: 400;
    font-size: 16px;
    letter-spacing: .04em;
  }

  .label--portrait { width: 318px; height: 512px; }
  .label--square { width: 396px; height: 397px; }

  .label--a { left: 58px; top: 346px; }
  .label--b { left: 402px; top: 43px; }
  .label--c { left: 402px; top: 461px; }
  .label--d { left: 825px; top: 346px; }

  .label--a .label__art { left: 94px; top: 194px; width: 150px; height: 150px; }
  .label--a .label__text { left: 58px; top: 56px; }
  .label--a .label__variety { font-size: 35px; line-height: 37px; }
  .label--a .label__vintage { font-size: 22px; margin-top: 4px; }
  .label--a .label__winery { left: 58px; top: 424px; }

  .label--b .label__art { left: 133px; top: 28px; width: 150px; height: 150px; }
  .label--b .label__text { left: 70px; top: 186px; }
  .label--b .label__variety { font-size: 31px; margin-top: 2px; }
  .label--b .label__vintage { font-size: 26px; margin-top: 1px; }
  .label--b .label__winery { left: 70px; top: 340px; }

  .label--c .label__art { left: 135px; top: 41px; width: 142px; height: 142px; }
  .label--c .label__text { left: 75px; top: 192px; }
  .label--c .label__variety { font-size: 29px; margin-top: 2px; }
  .label--c .label__vintage { font-size: 25px; margin-top: 1px; }
  .label--c .label__winery { left: 75px; top: 346px; }

  .label--d .label__art { left: 81px; top: 66px; width: 150px; height: 150px; }
  .label--d .label__text { left: 58px; top: 232px; }
  .label--d .label__variety { font-size: 35px; line-height: 37px; margin-top: 4px; }
  .label--d .label__vintage { font-size: 22px; margin-top: 4px; }
  .label--d .label__winery { left: 58px; top: 446px; }
</style>
</head>
<body>

<svg width="0" height="0" style="position:absolute">
  <defs>
    <linearGradient id="amber-fill" x1="0" y1="0" x2="1" y2="0">
      <stop offset="0" stop-color="#d18e2f"/>
      <stop offset="1" stop-color="#f8ad2a"/>
    </linearGradient>
  </defs>
</svg>

<!-- Portrait label, white ground -->
<div class="label label--portrait label--a">
  <svg class="label__stripes" viewBox="0 0 318 512" aria-hidden="true">
    <g fill="url(#amber-fill)">
      <polygon points="0,0 75,0 0,39"/>
      <polygon points="147,27 197,0 296,0 246,27"/>
      <polygon points="0,103 24,91 24,142 0,154"/>
      <polygon points="0,224 24,212 24,263 0,275"/>
      <polygon points="0,346 24,334 24,385 0,397"/>
      <polygon points="0,468 24,456 24,512 0,512"/>
      <polygon points="295,72 318,60 318,110 295,122"/>
      <polygon points="295,193 318,181 318,232 295,244"/>
      <polygon points="295,315 318,303 318,354 295,366"/>
      <polygon points="121,512 318,409 318,459 222,512"/>
    </g>
  </svg>
  <div class="label__text">
    <div class="label__variety">Grauer<br>Burgunder</div>
    <div class="label__vintage">Jahrgang 2021</div>
  </div>
  <div class="label__art" role="img" aria-label="Linienillustration: Frankfurter Skyline mit Mainbrücke über Weinbergreihen im Kreis"></div>
  <div class="label__winery">HABICHTSBERG</div>
</div>

<!-- Square label, corner band -->
<div class="label label--square label--b">
  <svg class="label__stripes" viewBox="0 0 396 397" aria-hidden="true">
    <polygon fill="url(#amber-fill)" points="186,397 396,285 396,397"/>
  </svg>
  <div class="label__art" role="img" aria-label="Linienillustration: Frankfurter Skyline mit Mainbrücke über Weinbergreihen im Kreis"></div>
  <div class="label__text">
    <div class="label__kicker">handarbeit</div>
    <div class="label__variety">Grauburgunder</div>
    <div class="label__vintage">Jahrgang 2021</div>
  </div>
  <div class="label__winery">HABICHTSBERG</div>
</div>

<!-- Square label, stripe frame -->
<div class="label label--square label--c">
  <svg class="label__stripes" viewBox="0 0 396 397" aria-hidden="true">
    <g fill="url(#amber-fill)">
      <polygon points="0,37 74,0 198,0 155,24 29,24 29,87 0,103"/>
      <polygon points="0,184 29,169 29,250 0,265"/>
      <polygon points="0,330 29,315 29,397 0,397"/>
      <polygon points="320,24 363,0 396,0 396,49 367,64 367,24"/>
      <polygon points="367,152 396,137 396,200 367,215"/>
      <polygon points="151,397 396,270 396,332 277,397"/>
    </g>
  </svg>
  <div class="label__art" role="img" aria-label="Linienillustration: Frankfurter Skyline mit Mainbrücke über Weinbergreihen im Kreis"></div>
  <div class="label__text">
    <div class="label__kicker">handarbeit</div>
    <div class="label__variety">Grauburgunder</div>
    <div class="label__vintage">Jahrgang 2021</div>
  </div>
  <div class="label__winery">HABICHTSBERG</div>
</div>

<!-- Portrait label, amber ground -->
<div class="label label--portrait label--amber label--d">
  <svg class="label__stripes" viewBox="0 0 318 512" aria-hidden="true">
    <g fill="#ffffff">
      <polygon points="0,0 75,0 0,39"/>
      <polygon points="147,27 197,0 296,0 246,27"/>
      <polygon points="0,103 24,91 24,142 0,154"/>
      <polygon points="0,224 24,212 24,263 0,275"/>
      <polygon points="0,346 24,334 24,385 0,397"/>
      <polygon points="0,468 24,456 24,512 0,512"/>
      <polygon points="295,72 318,60 318,110 295,122"/>
      <polygon points="295,193 318,181 318,232 295,244"/>
      <polygon points="295,315 318,303 318,354 295,366"/>
      <polygon points="121,512 318,409 318,459 222,512"/>
    </g>
  </svg>
  <div class="label__art" role="img" aria-label="Linienillustration: Frankfurter Skyline mit Mainbrücke über Weinbergreihen im Kreis"></div>
  <div class="label__text">
    <div class="label__kicker">handarbeit</div>
    <div class="label__variety">Grauer<br>Burgunder</div>
    <div class="label__vintage">Jahrgang 2021</div>
  </div>
  <div class="label__winery">HABICHTSBERG</div>
</div>

</body>
</html>
```